Communication and Marketing agency needs a new presentation card

We are a group of communication and marketing agencies specialized in companies that are in the logistics and industrial sector. The head agency is TELVANO Grupo and the group consists of 4 agencies: TELVANO Media, TELVANO Digital, TELVANO Research and EnlazaPorImagen. We hace 4 offices in Spain (Madrid, Barcelona, Valencia and Murcia). We are looking for a clean and attractive design that transmits our experience, brand presence in the market and knowledge to those who receive the card.It has to maintain the colors of the logo that is attached.
Target Market(s)
logistics and industrial sector
Marketing department
Clean and attractive design

```html
<!DOCTYPE html>
<html lang="es">
<head>
<meta charset="utf-8">
<title>TELVANO Grupo – Tarjeta de presentación</title>
<link href="https://fonts.googleapis.com/css2?family=Roboto:wght@300;400;500;700&display=swap" rel="stylesheet">
<style>
  :root {
    --brand-red: #ae2427;
    --ink: #4a4a4a;
    --ink-soft: #5a5a5a;
    --paper: #ffffff;
    --backdrop: #e4e4e4;
  }
  * { margin: 0; padding: 0; box-sizing: border-box; }
  html, body {
    width: 1125px; height: 1200px; overflow: hidden;
    background: var(--backdrop);
    font-family: "Roboto", Arial, sans-serif;
  }
  .card {
    position: absolute; left: 166px; width: 800px; height: 456px;
    box-shadow: 0 2px 4px rgba(0,0,0,.25);
  }
  .card--front { top: 103px; background: var(--paper); }
  .card--back { top: 619px; background: var(--brand-red); color: var(--paper); }

  .brand-mark { position: absolute; text-align: right; line-height: 1; }
  .brand-mark__name { display: block; font-weight: 300; letter-spacing: 1px; white-space: nowrap; }
  .brand-mark__unit { display: block; font-weight: 400; white-space: nowrap; }

  /* Front */
  .card--front .brand-mark { left: 40px; top: 56px; width: 355px; color: var(--brand-red); }
  .card--front .brand-mark__name { font-size: 76px; }
  .card--front .brand-mark__unit { font-size: 40px; color: var(--ink); margin-top: 0; }

  .name-band {
    position: absolute; left: 411px; top: 67px; width: 389px; height: 97px;
    background: var(--brand-red); color: var(--paper);
    text-align: right; padding: 22px 56px 0 0;
  }
  .name-band__name { font-size: 28px; font-weight: 700; line-height: 1.1; }
  .name-band__role { font-size: 20px; font-weight: 500; line-height: 1.2; }

  .contact-list {
    position: absolute; right: 56px; top: 237px; list-style: none;
    font-size: 19px; color: var(--ink-soft); text-align: right;
  }
  .contact-list li {
    display: flex; justify-content: flex-end; align-items: center;
    height: 25.3px; gap: 9px;
  }
  .contact-list svg { width: 18px; height: 18px; fill: var(--brand-red); flex: none; }
  .office-list {
    position: absolute; right: 54px; top: 377px;
    font-size: 19px; color: var(--ink-soft);
  }

  /* Back */
  .card--back .brand-mark { left: 150px; top: 142px; width: 456px; }
  .card--back .brand-mark__name { font-size: 92px; }
  .card--back .brand-mark__unit { font-size: 46px; margin-top: 0; }

  .agency-list {
    position: absolute; left: 92px; top: 372px;
    display: grid; grid-template-columns: repeat(4, 135px); column-gap: 30px;
    list-style: none;
  }
  .agency-list .brand-mark { position: static; width: 135px; }
  .agency-list .brand-mark__name { font-size: 25px; letter-spacing: 0; }
  .agency-list .brand-mark__unit { font-size: 15px; margin-top: 1px; }
  .agency-list .brand-mark--stacked { text-align: left; }
  .agency-list .brand-mark--stacked .brand-mark__name { font-size: 19px; line-height: 1.05; }
</style>
</head>
<body>

<section class="card card--front" aria-label="Anverso de la tarjeta">
  <div class="brand-mark">
    <span class="brand-mark__name">TELVANO</span>
    <span class="brand-mark__unit">Media</span>
  </div>

  <div class="name-band">
    <p class="name-band__name">Lorenzo Vidal</p>
    <p class="name-band__role">Director</p>
  </div>

  <ul class="contact-list">
    <li>910 555 204
      <svg viewBox="0 0 24 24" aria-hidden="true"><path d="M6.6 10.8a15.1 15.1 0 0 0 6.6 6.6l2.2-2.2c.3-.3.7-.4 1-.2 1.1.4 2.3.6 3.6.6.6 0 1 .4 1 1V20c0 .6-.4 1-1 1A17 17 0 0 1 3 4c0-.6.4-1 1-1h3.5c.6 0 1 .4 1 1 0 1.3.2 2.5.6 3.6.1.3 0 .7-.2 1z"/></svg>
    </li>
    <li>600 555 318
      <svg viewBox="0 0 24 24" aria-hidden="true"><path d="M7 1h10a2 2 0 0 1 2 2v18a2 2 0 0 1-2 2H7a2 2 0 0 1-2-2V3a2 2 0 0 1 2-2zm0 3v15h10V4zm5 16.2a1 1 0 1 0 0 .1z"/></svg>
    </li>
    <li>lvidal@telvano.es
      <svg viewBox="0 0 24 24" aria-hidden="true"><path d="M2 5h20v14H2zm2 2v.5l8 5.5 8-5.5V7zm0 3v7h16v-7l-8 5.5z"/></svg>
    </li>
    <li>lorenzovidal
      <svg viewBox="0 0 24 24" aria-hidden="true"><rect x="3" y="3" width="18" height="18" rx="2"/></svg>
    </li>
    <li>telvano.es
      <svg viewBox="0 0 24 24" aria-hidden="true"><circle cx="12" cy="12" r="10"/><path d="M8 6c2 1 1 3 3 4s0 3-1 5M15 5c-1 2 1 3 3 3M14 14c2 0 3 2 2 4" stroke="#fff" stroke-width="1.6" fill="none"/></svg>
    </li>
  </ul>

  <p class="office-list">Madrid | Barcelona | Valencia | Murcia</p>
</section>

<section class="card card--back" aria-label="Reverso de la tarjeta">
  <div class="brand-mark">
    <span class="brand-mark__name">TELVANO</span>
    <span class="brand-mark__unit">Grupo</span>
  </div>

  <ul class="agency-list">
    <li class="brand-mark"><span class="brand-mark__name">TELVANO</span><span class="brand-mark__unit">Digital</span></li>
    <li class="brand-mark"><span class="brand-mark__name">TELVANO</span><span class="brand-mark__unit">Media</span></li>
    <li class="brand-mark"><span class="brand-mark__name">TELVANO</span><span class="brand-mark__unit">Research</span></li>
    <li class="brand-mark brand-mark--stacked"><span class="brand-mark__name">ENLAZA<br>PORIMAGEN</span></li>
  </ul>
</section>

</body>
</html>
```